Letter Head / Envelopes
Business Card
Professional
Glen Hartwick Sr
Managing Partner
418 Tamsin Rd Ashbury, PA 19210
glen@copperfieldre.com
www.copperfieldre.com

```html
<!DOCTYPE html>
<html lang="en">
<head>
<meta charset="utf-8">
<title>Copperfield Real Estate — Stationery</title>
<link href="https://fonts.googleapis.com/css2?family=Cinzel:wght@700&family=Arimo:wght@400;700&display=swap" rel="stylesheet">
<style>
  :root {
    --backdrop: #7a5232;
    --paper: #ffffff;
    --maroon: #7d1d22;
    --ink: #3a3a3a;
    --faint: #e4e2df;
    --rule: #b9b9b9;
    --card-rule: #c9a9ab;
  }
  * { margin: 0; padding: 0; box-sizing: border-box; }
  html, body { width: 1200px; height: 766px; overflow: hidden; }
  body { background: var(--backdrop); font-family: "Arimo", Arial, sans-serif; color: var(--ink); position: relative; }
  address { font-style: normal; }

  .brand { display: flex; align-items: center; gap: 8px; }
  .brand-mark { width: 22px; height: 22px; background: var(--maroon); flex: none; }
  .brand-name { font-family: "Cinzel", Georgia, serif; font-weight: 700; color: var(--maroon); line-height: 1.02; font-size: 16px; letter-spacing: .3px; white-space: nowrap; }

  .letterhead { position: absolute; left: 34px; top: 91px; width: 518px; height: 629px; background: var(--paper); box-shadow: 0 3px 10px rgba(0,0,0,.35); overflow: hidden; }
  .letterhead .header { position: absolute; left: 22px; top: 26px; display: flex; align-items: flex-start; gap: 12px; }
  .letterhead .header .brand { padding-top: 6px; }
  .letterhead .contact { border-left: 1px solid var(--rule); padding-left: 10px; font-size: 7.5px; line-height: 1.45; color: var(--ink); }

  .watermark { position: absolute; display: flex; flex-direction: column; align-items: center; gap: 8px; }
  .watermark .mark { background: var(--faint); }
  .watermark .name { font-family: "Cinzel", Georgia, serif; font-weight: 700; color: var(--faint); text-align: center; line-height: 1; white-space: nowrap; }
  .letterhead .watermark { left: 330px; top: 452px; width: 170px; }
  .letterhead .watermark .mark { width: 90px; height: 90px; }
  .letterhead .watermark .name { font-size: 20px; }

  .business-card { position: absolute; left: 713px; top: 163px; width: 240px; height: 150px; background: var(--paper); box-shadow: 0 3px 8px rgba(0,0,0,.35); overflow: hidden; }
  .business-card .card-band { position: absolute; left: 0; top: 0; }
  .business-card .card-person { position: absolute; left: 11px; top: 14px; color: #fff; font-size: 7px; line-height: 1.4; }
  .business-card .card-person .name { font-weight: 700; font-size: 8px; }
  .business-card .card-contact { position: absolute; left: 11px; top: 70px; color: #fff; font-size: 5.5px; line-height: 1.5; }
  .business-card .brand { position: absolute; left: 124px; top: 60px; gap: 5px; }
  .business-card .brand-mark { width: 14px; height: 14px; }
  .business-card .brand-name { font-size: 10.5px; }

  .envelope { position: absolute; left: 600px; top: 384px; width: 571px; height: 336px; background: var(--paper); box-shadow: 0 3px 10px rgba(0,0,0,.35); overflow: hidden; }
  .envelope .flap-line { position: absolute; left: 0; top: 0; }
  .envelope .return { position: absolute; left: 22px; top: 126px; display: flex; align-items: center; gap: 10px; }
  .envelope .return .contact { border-left: 1px solid var(--rule); padding-left: 8px; font-size: 7px; line-height: 1.45; }
  .envelope .watermark { right: 18px; top: 214px; width: 120px; }
  .envelope .watermark .mark { width: 56px; height: 56px; }
  .envelope .watermark .name { font-size: 12px; }
</style>
</head>
<body>

  <section class="letterhead">
    <header class="header">
      <div class="brand">
        <span class="brand-mark"></span>
        <span class="brand-name">COPPERFIELD<br>REAL ESTATE</span>
      </div>
      <address class="contact">
        418 Tamsin Rd<br>
        Ashbury, PA 19210<br>
        Phone: 484-555-0192<br>
        Fax: 484-555-0187<br>
        www.copperfieldre.com
      </address>
    </header>
    <div class="watermark">
      <span class="mark"></span>
      <span class="name">COPPERFIELD<br>REAL ESTATE</span>
    </div>
  </section>

  <section class="business-card">
    <svg class="card-band" width="240" height="150" viewBox="0 0 240 150">
      <path d="M0 0 H114 C96 34 96 116 114 150 H0 Z" fill="var(--maroon)"/>
      <path d="M114 0 C96 34 96 116 114 150" fill="none" stroke="var(--card-rule)" stroke-width="2"/>
    </svg>
    <div class="card-person">
      <div class="name">Glen Hartwick Sr</div>
      <div>Managing Partner</div>
    </div>
    <address class="card-contact">
      418 Tamsin Rd<br>
      Ashbury, PA 19210<br>
      Phone 484-555-0192<br>
      Cell 484-555-0163<br>
      Fax 484-555-0187<br>
      glen@copperfieldre.com<br>
      www.copperfieldre.com
    </address>
    <div class="brand">
      <span class="brand-mark"></span>
      <span class="brand-name">COPPERFIELD<br>REAL ESTATE</span>
    </div>
  </section>

  <section class="envelope">
    <svg class="flap-line" width="571" height="70" viewBox="0 0 571 70">
      <path d="M0 1 L34 62 H537 L571 1" fill="none" stroke="#dcdcdc" stroke-width="1"/>
    </svg>
    <div class="return">
      <div class="brand">
        <span class="brand-mark"></span>
        <span class="brand-name">COPPERFIELD<br>REAL ESTATE</span>
      </div>
      <address class="contact">
        418 Tamsin Rd<br>
        Ashbury, PA 19210
      </address>
    </div>
    <div class="watermark">
      <span class="mark"></span>
      <span class="name">COPPERFIELD<br>REAL ESTATE</span>
    </div>
  </section>

</body>
</html>
```